Business Card Design for Animal Clinic

We are seeking a two sided business card design. The primary side should include our logo (provided in AI and EPS files) address, phone, website, and if possible "Follow Us" with icons for Facebook, Google+, and Twitter.

The back of the card needs to included space for appointment reminders.

Company Name:
Calderbrook Animal Clinic

Doctor Name:
To be provided to winner

Adress:
To be provided to winner

Phone:
to be provided to winner

Website:
www.calderbrookanimalclinic.com

```html
<!DOCTYPE html>
<html lang="en">
<head>
<meta charset="utf-8">
<title>Calderbrook Animal Clinic – Business Card</title>
<link rel="stylesheet" href="https://fonts.googleapis.com/css2?family=Cinzel:wght@700&family=Marcellus&family=Crimson+Text:wght@400;700&family=Lato:wght@400;700&family=Montserrat:wght@600&display=swap">
<style>
  :root {
    --clinic-red: #a8392e;
    --card-black: #060606;
    --card-white: #ffffff;
    --backdrop: #e4e4e4;
    --rule-grey: #8a8a8a;
    --ink: #1e1e1e;
  }
  * { box-sizing: border-box; margin: 0; padding: 0; }
  html, body {
    width: 1200px; height: 926px; overflow: hidden;
    background: var(--backdrop);
  }
  .canvas {
    position: relative; width: 1200px; height: 926px;
  }
  .card {
    position: absolute; left: 250px; width: 700px; height: 400px;
    background: var(--card-white);
    box-shadow: 0 6px 18px rgba(0,0,0,0.18);
    overflow: hidden;
  }
  .card--front { top: 42px; }
  .card--back { top: 484px; }

  /* Front */
  .front-logo {
    position: absolute; top: 0; left: 0; width: 100%; height: 135px;
    display: flex; flex-direction: column; align-items: center; justify-content: center;
    color: var(--clinic-red);
    font-family: "Marcellus", serif; font-weight: 400;
  }
  .front-logo__name { font-size: 46px; letter-spacing: 2px; line-height: 1; }
  .front-logo__sub { font-size: 20px; letter-spacing: 6px; margin-top: 8px; }
  .front-band {
    position: absolute; top: 135px; left: 0; width: 100%; height: 45px;
    background: var(--clinic-red);
    display: flex; align-items: center; justify-content: flex-end; padding-right: 40px;
    color: var(--card-white);
    font-family: "Cinzel", serif; font-weight: 700; font-size: 21px; letter-spacing: 3px;
  }
  .front-body {
    position: absolute; top: 180px; left: 0; width: 100%; height: 220px;
    background: var(--card-black);
    color: var(--card-white);
  }
  .person { position: absolute; left: 36px; top: 10px; }
  .person__name {
    font-family: "Crimson Text", serif; font-size: 38px; line-height: 1.1;
  }
  .person__name strong { font-weight: 700; }
  .person__title {
    font-family: "Crimson Text", serif; font-size: 15px; letter-spacing: 2px;
    color: var(--clinic-red); text-transform: uppercase;
  }
  .contacts { position: absolute; left: 36px; top: 92px; list-style: none; }
  .contacts li {
    display: flex; align-items: center; gap: 12px;
    font-family: "Crimson Text", serif; font-size: 17px; line-height: 24px;
  }
  .contacts svg { width: 14px; height: 14px; fill: var(--clinic-red); flex: none; }
  .follow {
    position: absolute; right: 36px; top: 108px;
    display: flex; align-items: center; gap: 8px;
    font-family: "Crimson Text", serif; font-size: 15px; letter-spacing: 1px;
  }
  .follow__dot {
    width: 20px; height: 20px; border-radius: 50%; background: var(--card-white);
  }

  /* Back */
  .appointment__title {
    position: absolute; top: 34px; left: 0; width: 100%; text-align: center;
    font-family: "Montserrat", sans-serif; font-weight: 600; font-size: 24px; letter-spacing: 2px;
    color: var(--ink);
  }
  .appointment__fields { position: absolute; top: 88px; left: 40px; right: 40px; }
  .field {
    display: flex; align-items: flex-end; gap: 14px; height: 46px;
    font-family: "Lato", sans-serif; font-size: 18px; color: var(--ink);
  }
  .field__line { flex: 1; border-bottom: 1.5px solid var(--rule-grey); margin-bottom: 4px; }
  .back-band {
    position: absolute; left: 0; bottom: 0; width: 100%; height: 145px;
    background: var(--clinic-red);
    display: flex; align-items: center; justify-content: center; text-align: center;
    color: var(--card-white);
    font-family: "Lato", sans-serif; font-size: 20px; letter-spacing: 1.5px; line-height: 1.5;
  }
</style>
</head>
<body>
<main class="canvas">
  <section class="card card--front">
    <div class="front-logo">
      <span class="front-logo__name">CALDERBROOK</span>
      <span class="front-logo__sub">ANIMAL CLINIC</span>
    </div>
    <div class="front-band">CALDERBROOK ANIMAL CLINIC</div>
    <div class="front-body">
      <div class="person">
        <p class="person__name">Daniel <strong>Hartley</strong></p>
        <p class="person__title">Veterinary Doctor</p>
      </div>
      <ul class="contacts">
        <li><svg viewBox="0 0 16 16"><path d="M3 1h3l1.5 4-2 1.3a9 9 0 0 0 4.2 4.2l1.3-2 4 1.5v3a2 2 0 0 1-2 2A13 13 0 0 1 1 3a2 2 0 0 1 2-2z"/></svg>555-014-2290</li>
        <li><svg viewBox="0 0 16 16"><path d="M1 3h14v10H1z M1 3l7 6 7-6" fill="none" stroke="#a8392e" stroke-width="1.8"/></svg>yourdomain.com</li>
        <li><svg viewBox="0 0 16 16"><path d="M6.5 9.5l3-3 M7 4.5l1.5-1.5a3 3 0 0 1 4.5 4.5L11.5 9 M9 11.5L7.5 13A3 3 0 0 1 3 8.5L4.5 7" fill="none" stroke="#a8392e" stroke-width="2" stroke-linecap="round"/></svg>yourname@yourdomain.com</li>
        <li><svg viewBox="0 0 16 16"><path d="M8 1l7 6.5h-2.2V15H9.8v-4.5H6.2V15H3.2V7.5H1z"/></svg>Street address goes here, Suite #303, Alt Bldg, NY 82365</li>
      </ul>
      <div class="follow">
        <span>FOLLOW US :</span>
        <span class="follow__dot"></span>
        <span class="follow__dot"></span>
        <span class="follow__dot"></span>
      </div>
    </div>
  </section>

  <section class="card card--back">
    <h2 class="appointment__title">APPOINTMENT</h2>
    <div class="appointment__fields">
      <div class="field"><span>Date:</span><span class="field__line"></span></div>
      <div class="field"><span>Time:</span><span class="field__line"></span></div>
      <div class="field"><span>Location:</span><span class="field__line"></span></div>
    </div>
    <div class="back-band">
      <p>Street address goes here, Suite #303,<br>Alt Bldg, NY 82365</p>
    </div>
  </section>
</main>
</body>
</html>
```